Billboard for personal injury chiropractors office

We are a personal injury chiropractor clinic.
I need a Billboard with the company name as the dominating factor. Also a smaller picture or 2 of something creative, like a car accident or an arm in a cast off to the sides.
We Like something Clean and Simple and Eye Catching. Please make the picture Small and Off To The Side. The MAIN FOCUS areas are the… name Varden Chiropractic Clinic
At the top CAR ACCIDENT INJURY?
AND at the bottom our number 418-27-FLEXA.
Dr.Milo R. Varden in bold somewhere with the word chiropractor under the doctors name in a text.

Im open to red lettering on white backgrounds, red on yellow backgrounds and I'm also open to reds blues white and yellow. I'd prefer yellow if used be across the bottom.

I am uploading a very rough draft of what we are after along with a screenshot of the tv commercial showing the yellow

DO NOT USE THE LOGO ON THE COMMERCIAL. I JUST WANT THE NAME TYPED LIKE ON SAMPLE BILLBOARD.

Industry/Entity Type

Chiropractic

Colors
0054AA
0677BA
7BADD7
CADEEF
E8F1F8
FFF300
FFF600
FEFA6F
FFFEC7
FFFEE8
EB3D1F
EC4F4E
F09395
F8D3D4
FCEDEE

Requirements
Must have
• Eye catching ,bold

```html
<!DOCTYPE html>
<html lang="en">
<head>
<meta charset="utf-8">
<title>Varden Chiropractic Clinic Billboard</title>
<link rel="stylesheet" href="https://fonts.googleapis.com/css2?family=Bebas+Neue&family=Montserrat:wght@400;700;800&display=swap">
<style>
  :root {
    --stage: #a5a5a5;
    --brand-blue: #0677ba;
    --ink-blue: #0a6fb4;
    --sun-yellow: #fff600;
    --paper: #ffffff;
    --ink: #111111;
    --mint: #c4f7e8;
  }
  html, body {
    margin: 0;
    width: 1200px;
    height: 1200px;
    overflow: hidden;
    background: var(--stage);
  }
  .billboard {
    position: absolute;
    left: 50px;
    top: 440px;
    width: 1100px;
    height: 320px;
    background: var(--paper);
    box-shadow: 10px 12px 10px rgba(0,0,0,0.35);
    overflow: hidden;
  }
  .billboard__shapes {
    position: absolute;
    inset: 0;
    width: 1100px;
    height: 320px;
  }
  .clinic-name {
    position: absolute;
    left: 34px;
    top: 30px;
    margin: 0;
    font-family: "Bebas Neue", sans-serif;
    font-weight: 400;
    font-size: 62px;
    line-height: 1;
    letter-spacing: 0;
    color: var(--paper);
    white-space: nowrap;
  }
  .headline {
    position: absolute;
    left: 34px;
    top: 112px;
    margin: 0;
    font-family: "Montserrat", sans-serif;
    font-weight: 800;
    font-size: 40px;
    line-height: 53px;
    color: var(--sun-yellow);
    white-space: nowrap;
  }
  .doctor {
    position: absolute;
    left: 34px;
    top: 268px;
    margin: 0;
    font-family: "Montserrat", sans-serif;
    font-size: 25px;
    line-height: 1;
    white-space: nowrap;
  }
  .doctor__name { font-weight: 700; color: var(--ink-blue); }
  .doctor__surname { font-weight: 700; font-size: 22px; color: var(--ink); }
  .doctor__title { font-weight: 400; font-size: 22px; color: var(--ink); }
  .phone {
    position: absolute;
    left: 640px;
    width: 420px;
    top: 258px;
    margin: 0;
    text-align: center;
    font-family: "Montserrat", sans-serif;
    font-weight: 700;
    font-size: 48px;
    line-height: 1;
    letter-spacing: 1px;
    color: var(--ink-blue);
    white-space: nowrap;
  }
</style>
</head>
<body>
  <section class="billboard">
    <svg class="billboard__shapes" viewBox="0 0 1100 320" xmlns="http://www.w3.org/2000/svg">
      <defs>
        <linearGradient id="photoTone" x1="0" y1="0" x2="1" y2="1">
          <stop offset="0" stop-color="#e9eef0"/>
          <stop offset="0.45" stop-color="#c4f7e8"/>
          <stop offset="1" stop-color="#4a4d52"/>
        </linearGradient>
      </defs>
      <polygon class="photo-area" role="img" aria-label="Photo: man with a bandaged arm standing beside a car with a crushed front end" points="700,0 1100,0 1100,250 600,250" fill="url(#photoTone)"/>
      <polygon class="blue-panel" points="0,0 706,0 614,250 0,250" fill="var(--brand-blue)"/>
      <polygon class="yellow-band" points="614,250 1100,250 1100,320 585,320" fill="var(--sun-yellow)"/>
    </svg>

    <h1 class="clinic-name">VARDEN CHIROPRACTIC CLINIC</h1>
    <p class="headline">AT THE TOP<br>CAR ACCIDENT INJURY?</p>
    <p class="doctor"><span class="doctor__name">DR.MILO R.</span> <span class="doctor__surname">VARDEN</span> <span class="doctor__title">Chiropractor</span></p>
    <p class="phone">418-27-FLEXA</p>
  </section>
</body>
</html>
```